Business Card Design Project

Hello Designers, hope you are all aiming enjoy the weekend
I have the Business Logo (uploaded), you can alter the color which ever way you think would work,
Im looking for a simple yet striking feel, something which will stay memorable (I have uploaded 3 examples for you to flick through)
Information on the card, will just be the bare minimum,
Double Sided
Info being
i.e.
Name
Number
Website
ABN
Tobin Wexmoor
+468213579 (singapore)
+315792846 (Australia)
+729384615 (America)
www.lomevu-linkup.example
ABN 86420913
Enjoy,
Tobin
Industry/Entity Type
Business
Look and feel
Each slider illustrates characteristics of the customer's brand and the style your logo design should communicate.

```html
<!DOCTYPE html>
<html lang="en">
<head>
<meta charset="utf-8">
<title>Lomevu Linkup — Business Card</title>
<link href="https://fonts.googleapis.com/css2?family=Open+Sans:wght@400;600&display=swap" rel="stylesheet">
<style>
  :root {
    --backdrop: #d9d4cf;
    --card-black: #000000;
    --band-dark: #141414;
    --band-info: #121212;
    --brand-grey: #5e5e5e;
    --brand-crimson: #c41f43;
    --info-text: #e8e8e8;
  }
  * { margin: 0; padding: 0; box-sizing: border-box; }
  html, body {
    width: 1200px;
    height: 960px;
    overflow: hidden;
    background: var(--backdrop);
    font-family: "Open Sans", Arial, sans-serif;
  }
  .stage { position: relative; width: 1200px; height: 960px; }
  .card {
    position: absolute;
    width: 707px;
    height: 403px;
    background: var(--card-black);
    overflow: hidden;
  }
  .card--front { left: 79px; top: 82px; }
  .card--back { left: 434px; top: 525px; }

  .front-band {
    position: absolute;
    left: 0; top: 139px;
    width: 100%; height: 120px;
    background: var(--band-dark);
    display: flex;
    align-items: center;
    justify-content: center;
    gap: 20px;
  }
  .brand-mark {
    display: block;
    background: var(--brand-crimson);
    border-radius: 12px;
  }
  .front-band .brand-mark { width: 60px; height: 60px; }
  .brand-name {
    font-family: "Open Sans", Arial, sans-serif;
    font-weight: 600;
    color: var(--brand-grey);
    letter-spacing: 0.5px;
    white-space: nowrap;
  }
  .front-band .brand-name { font-size: 50px; }

  .back-brand {
    position: absolute;
    left: 0; top: 0;
    width: 100%; height: 244px;
    display: flex;
    flex-direction: column;
    align-items: center;
    justify-content: center;
    gap: 10px;
    padding-top: 20px;
  }
  .back-brand .brand-mark { width: 106px; height: 106px; border-radius: 16px; margin-left: 2px; }
  .back-brand .brand-name { font-size: 54px; line-height: 1.1; }

  .info-band {
    position: absolute;
    left: 0; top: 244px;
    width: 100%; height: 159px;
    background: var(--band-info);
    padding: 26px 0 0 36px;
    color: var(--info-text);
    font-size: 14.5px;
    list-style: none;
  }
  .info-band li { line-height: 15px; margin-bottom: 16px; }
</style>
</head>
<body>
<main class="stage">
  <section class="card card--front" aria-label="Card front">
    <div class="front-band">
      <span class="brand-mark" aria-hidden="true"></span>
      <span class="brand-name">Lomevu Linkup</span>
    </div>
  </section>

  <section class="card card--back" aria-label="Card back">
    <div class="back-brand">
      <span class="brand-mark" aria-hidden="true"></span>
      <span class="brand-name">Lomevu Linkup</span>
    </div>
    <ul class="info-band">
      <li class="info-name">Tobin Wexmoor</li>
      <li class="info-phone">Tel &nbsp;: +468213579 (Singapore) | +315792846 (Australia) | +729384615 (Amerika)</li>
      <li class="info-web">www.lomevu-linkup.example</li>
      <li class="info-abn">ABN 86420913</li>
    </ul>
  </section>
</main>
</body>
</html>
```